Bramblecrest Apparel and Nutrition is looking for a Clothing/Supplement Online Store Website!

Must be convenient, and user friendly, with vibrant colors that catch the eye!

Target Market(s)

Athletes, and Fashion Customers

Industry/Entity Type

Fitness

Coding

Coded - Design and coding required

Number of Pages Required

3 page

Font styles to use
Decorative

Colors

Designer to choose colors to be used in the design.

Requirements
Must have
• Somewhere to feature products, features to promote discounts and make announcements.
Nice to have
• My logos on each page

```html
<!DOCTYPE html>
<html lang="en">
<head>
<meta charset="utf-8">
<title>Bramblecrest Apparel and Nutrition</title>
<link rel="stylesheet" href="https://fonts.googleapis.com/css2?family=Open+Sans:wght@400;600;700;800&display=swap">
<style>
:root{
  --red:#e5353f;
  --pink:#fcd4d8;
  --pink-soft:#fde6e8;
  --teal:#7ccfbe;
  --ink:#1e1e1e;
  --text:#555;
  --muted:#999;
  --line:#e6e6e6;
  --gray:#f3f3f3;
  --gold:#f5b301;
  --white:#fff;
}
*{box-sizing:border-box;margin:0;padding:0}
html,body{width:1200px;height:3820px;overflow:hidden}
body{font-family:"Open Sans",Arial,sans-serif;color:var(--ink);background:var(--white);position:relative;font-size:13px}
.wrap{width:880px;margin:0 auto;position:relative}
a{color:inherit;text-decoration:none}

/* top bar */
.topbar{height:32px;border-bottom:1px solid var(--line);font-size:10px;color:var(--muted)}
.topbar .wrap{display:flex;justify-content:space-between;align-items:center;height:32px}
.topbar .links{display:flex;gap:22px}

/* header */
.header{height:72px}
.header .wrap{display:flex;align-items:center;height:72px}
.brand{display:flex;align-items:center;gap:8px;font-weight:800;font-size:20px;color:var(--ink);letter-spacing:.5px}
.brand .dot{width:12px;height:12px;background:var(--red)}
.nav{display:flex;gap:22px;margin-left:170px;font-size:11px;font-weight:700}
.nav .active{color:var(--red)}
.tools{margin-left:auto;display:flex;gap:16px}
.tools svg{width:16px;height:16px;stroke:var(--ink);fill:none;stroke-width:1.6}

/* hero */
.hero{position:relative;height:496px;margin-top:6px}
.hero-shade{position:absolute;left:0;top:0;width:660px;height:496px;background:var(--gray)}
.hero-photo{position:absolute;left:240px;top:0;width:420px;height:496px;background:linear-gradient(160deg,#dfe6ee,#8ea5bf 55%,#3b4f6b)}
.hero-copy{position:absolute;left:552px;top:108px}
.hero-copy .num{font-size:16px;font-weight:700;margin-bottom:18px}
.hero-copy h1{font-size:56px;line-height:66px;font-weight:800}
.hero-pager{position:absolute;left:160px;top:418px;display:flex;align-items:center;gap:10px;font-size:13px}
.hero-pager span.bar{width:60px;height:1px;background:var(--ink)}

/* features */
.features{display:flex;gap:40px;margin-top:50px}
.feature{flex:1;height:170px;border:1px solid var(--line);text-align:center;padding-top:26px}
.feature .icon{width:44px;height:44px;border-radius:50%;background:#e4f5f1;margin:0 auto 16px;display:flex;align-items:center;justify-content:center}
.feature .icon svg{width:20px;height:20px;stroke:var(--teal);fill:none;stroke-width:1.8}
.feature h4{font-size:11px;font-weight:700;margin-bottom:8px}
.feature p{font-size:10px;color:var(--muted);line-height:15px;padding:0 40px}

/* section titles */
.section-title{text-align:center}
.section-title h2{font-size:30px;font-weight:600}
.section-title p{font-size:10px;color:var(--muted);margin-top:6px}

/* products */
.grid{display:grid;grid-template-columns:repeat(4,208px);gap:16px}
.card .thumb{position:relative;height:260px;background:var(--gray)}
.card .thumb .img{position:absolute;inset:28px 40px}
.badge{position:absolute;top:12px;font-size:9px;font-weight:700;color:var(--white)}
.badge.sale{left:12px;background:var(--red);padding:5px 10px}
.badge.new{left:12px;width:34px;height:34px;border-radius:50%;background:var(--teal);display:flex;align-items:center;justify-content:center}
.card .meta{display:flex;justify-content:space-between;font-size:11px;margin-top:12px;color:var(--text)}
.card .price{font-size:15px;font-weight:700;margin-top:4px;display:block}
.stars{color:var(--gold);letter-spacing:1px}
.stars .off{color:#ccc}
.add{position:absolute;left:12px;bottom:12px;font-size:10px;font-weight:700;color:var(--red)}
.quick{position:absolute;right:12px;top:12px;display:flex;flex-direction:column;gap:10px}
.quick span{width:22px;height:22px;border-radius:50%;background:var(--white)}

.dots{display:flex;justify-content:center;gap:6px;margin-top:34px}
.dots span{width:8px;height:8px;border-radius:50%;background:#ccc}
.dots span.on{background:var(--ink)}

/* promos */
.promos{display:flex;gap:16px;margin-top:56px}
.promo{position:relative;flex:1;height:180px;background:var(--pink);overflow:hidden}
.promo .txt{position:absolute;left:34px;top:40px}
.promo h3{font-size:48px;line-height:46px;font-weight:800;color:var(--ink)}
.promo p{font-size:13px;font-weight:600;margin-top:10px;letter-spacing:1px}
.promo p b{color:var(--red)}
.promo .img{position:absolute;right:26px;top:22px;width:170px;height:136px}

/* tabs */
.tabs{display:flex;justify-content:center;gap:18px;margin-top:18px;font-size:10px;font-weight:700;color:var(--text)}
.tabs .on{background:var(--red);color:var(--white);padding:2px 10px;border-radius:10px}

.pager{display:flex;justify-content:center;gap:8px;margin-top:44px;font-size:10px}
.pager span{min-width:26px;height:26px;border:1px solid var(--line);display:flex;align-items:center;justify-content:center;padding:0 6px}
.pager .on{background:var(--ink);color:var(--white);border-color:var(--ink)}

/* summer */
.summer{position:relative;height:320px;background:var(--pink);margin-top:50px}
.summer .clothes{position:absolute;left:160px;top:50px;width:380px;height:220px}
.summer .copy{position:absolute;left:560px;top:76px;width:260px;text-align:center}
.summer .copy small{font-size:13px;letter-spacing:2px;font-weight:600}
.summer .copy h3{font-size:36px;line-height:42px;font-weight:800;margin-top:6px}
.summer .copy p{font-size:14px;margin-top:10px;letter-spacing:1px}
.summer .copy p b{color:var(--red)}
.summer .tub{position:absolute;left:820px;top:30px;width:200px;height:250px}

/* blog */
.blog{display:flex;gap:20px;margin-top:80px}
.blog-intro{width:280px}
.blog-intro h2{font-size:30px;font-weight:600}
.blog-intro p{font-size:10px;color:var(--muted);margin-top:6px}
.btn{display:inline-block;background:var(--ink);color:var(--white);font-size:10px;font-weight:700;padding:9px 20px;margin-top:22px}
.post{width:280px}
.post .img{height:180px}
.post .date{font-size:10px;color:var(--muted);margin-top:16px}
.post h4{font-size:13px;font-weight:700;margin-top:6px}
.post p{font-size:10px;color:var(--muted);line-height:16px;margin-top:8px}
.post .more{display:inline-block;font-size:10px;font-weight:700;margin-top:12px;border-bottom:1px solid var(--ink)}

/* footer */
.footer{position:absolute;left:0;top:3390px;width:1200px;height:430px;background:var(--gray)}
.footer .top{display:flex;align-items:flex-start;padding-top:60px}
.footer .brand{font-size:24px}
.newsletter{margin-left:130px;width:250px}
.newsletter h5{font-size:14px;font-weight:700}
.newsletter p{font-size:10px;color:var(--muted);margin-top:6px;line-height:15px}
.subscribe{margin-left:auto;display:flex;margin-top:16px}
.subscribe .field{width:190px;height:30px;background:var(--white);font-size:10px;color:var(--muted);padding:9px 10px}
.subscribe .go{height:30px;background:var(--ink);color:var(--white);font-size:10px;font-weight:700;padding:9px 14px}
.cols{display:flex;margin-top:46px}
.col h6{font-size:12px;font-weight:700;margin-bottom:14px}
.col li{list-style:none;font-size:10px;color:var(--text);margin-bottom:8px}
.col.touch{width:300px}
.col.touch li{display:flex;gap:10px;margin-bottom:14px}
.col.touch svg{width:14px;height:14px;stroke:var(--ink);fill:none;stroke-width:1.6;flex:none}
.col.touch b{display:block;font-size:10px}
.col.std{width:215px}
.col.last{margin-left:auto;width:auto}
.bottom{position:absolute;left:160px;right:160px;top:370px;display:flex;justify-content:space-between;align-items:center;font-size:10px;color:var(--muted)}
.cards{display:flex;gap:4px}
.cards span{width:28px;height:18px;border-radius:2px;background:#d6dbe4}
.totop{position:absolute;right:18px;bottom:18px;width:30px;height:30px;background:var(--ink);display:flex;align-items:center;justify-content:center}
.totop svg{width:12px;height:12px;stroke:var(--white);fill:none;stroke-width:2}
</style>
</head>
<body>

<div class="topbar"><div class="wrap">
  <span>+1 800 555 0142</span>
  <div class="links"><span>Welcome to our store</span><span>+1 800 555 0199</span><span>My account</span><span>Sign in</span></div>
</div></div>

<header class="header"><div class="wrap">
  <div class="brand"><span class="dot"></span>Bramblecrest</div>
  <nav class="nav"><a class="active">HOME</a><a>SHOP</a><a>MEN</a><a>WOMEN</a><a>SUPPLEMENT</a><a>BLOG</a></nav>
  <div class="tools">
    <svg viewBox="0 0 16 16"><circle cx="7" cy="7" r="5"/><path d="M11 11l4 4"/></svg>
    <svg viewBox="0 0 16 16"><circle cx="8" cy="5" r="3"/><path d="M2 15c1-4 11-4 12 0"/></svg>
    <svg viewBox="0 0 16 16"><path d="M8 14s-6-4-6-8a3 3 0 0 1 6-1 3 3 0 0 1 6 1c0 4-6 8-6 8z"/></svg>
    <svg viewBox="0 0 16 16"><path d="M2 3h2l2 8h7l2-6H5"/><circle cx="7" cy="14" r="1"/><circle cx="12" cy="14" r="1"/></svg>
  </div>
</div></header>

<section class="hero">
  <div class="hero-shade"></div>
  <div class="hero-photo" role="img" aria-label="Young man in a denim jacket posing"></div>
  <div class="hero-copy">
    <div class="num">01/</div>
    <h1>Simplycity<br>Freedom<br>comfort</h1>
  </div>
  <div class="hero-pager"><span>1</span><span class="bar"></span><span>3</span></div>
</section>

<div class="wrap">
  <div class="features">
    <div class="feature">
      <div class="icon"><svg viewBox="0 0 20 20"><path d="M4 10l4 4 8-8"/></svg></div>
      <h4>100% SATISFACTION</h4><p>Quality you can trust on every order</p>
    </div>
    <div class="feature">
      <div class="icon"><svg viewBox="0 0 20 20"><circle cx="10" cy="10" r="7"/><path d="M10 6v4l3 2"/></svg></div>
      <h4>30 DAYS MONEY BACK</h4><p>Return any item within thirty days for a full refund</p>
    </div>
    <div class="feature">
      <div class="icon"><svg viewBox="0 0 20 20"><path d="M2 6h10v8H2zM12 9h4l2 3v2h-6"/><circle cx="6" cy="15" r="1.5"/><circle cx="15" cy="15" r="1.5"/></svg></div>
      <h4>FAST DELIVERY</h4><p>We ship quickly to your door with tracking on all orders</p>
    </div>
  </div>

  <div class="section-title" style="margin-top:76px"><h2>New Arrivals</h2><p>Fresh styles and supplements just landed</p></div>

  <div class="grid" style="margin-top:40px">
    <div class="card"><div class="thumb"><div class="img" role="img" aria-label="Red polka dot dress" style="background:linear-gradient(#e64a52,#b8222c)"></div><div class="quick"><span></span><span></span></div><span class="add">+ ADD TO CART</span></div><div class="meta"><span>Items product title</span><span class="stars">★★★<span class="off">★★</span></span></div><span class="price">$50.00</span></div>
    <div class="card"><div class="thumb"><div class="img" role="img" aria-label="Pink checked shirt" style="background:linear-gradient(#f0d6d8,#c99aa0)"></div></div><div class="meta"><span>Items product title</span><span class="stars">★★★<span class="off">★★</span></span></div><span class="price">$50.00</span></div>
    <div class="card"><div class="thumb"><span class="badge sale">SOLD OUT</span><div class="img" role="img" aria-label="Blue denim jeans" style="background:linear-gradient(#9db6d6,#4d6c96)"></div></div><div class="meta"><span>Items product title</span><span class="stars">★★★<span class="off">★★</span></span></div><span class="price">$50.00</span></div>
    <div class="card"><div class="thumb"><span class="badge new">NEW</span><div class="img" role="img" aria-label="Tub of whey protein" style="background:linear-gradient(#3a3a3a,#111)"></div></div><div class="meta"><span>Items product title</span><span class="stars">★★★<span class="off">★★</span></span></div><span class="price">$75.00</span></div>
  </div>
  <div class="dots"><span class="on"></span><span></span><span></span></div>

  <div class="promos">
    <div class="promo"><div class="txt"><h3>FINAL<br>SALE</h3><p>UP TO <b>60%</b> OFF</p></div><div class="img" role="img" aria-label="Folded plaid shirts" style="background:linear-gradient(135deg,#c84a4a,#3b3b3b)"></div></div>
    <div class="promo"><div class="txt"><h3>FLASH<br>DEAL</h3><p>MEGA OFFER <b>50%</b> OFF</p></div><div class="img" role="img" aria-label="Protein shaker and supplement tub" style="background:linear-gradient(135deg,#7a7a7a,#151515)"></div></div>
  </div>

  <div class="section-title" style="margin-top:58px"><h2>New Arrivals</h2><p>Fresh styles and supplements just landed</p></div>
  <div class="tabs"><span class="on">ALL</span><span>MEN</span><span>WOMEN</span><span>KIDS</span><span>SUPPLEMENT</span></div>

  <div class="grid" style="margin-top:30px;row-gap:40px">
    <div class="card"><div class="thumb"><div class="img" role="img" aria-label="Black and pink party dress" style="background:linear-gradient(#e0a3c0,#222)"></div></div><div class="meta"><span>Items product title</span><span class="stars">★★★<span class="off">★★</span></span></div><span class="price">$50.00</span></div>
    <div class="card"><div class="thumb"><div class="img" role="img" aria-label="Navy button shirt" style="background:linear-gradient(#5574a8,#243a66)"></div></div><div class="meta"><span>Items product title</span><span class="stars">★★★<span class="off">★★</span></span></div><span class="price">$50.00</span></div>
    <div class="card"><div class="thumb"><span class="badge sale">SOLD OUT</span><div class="img" role="img" aria-label="Protein powder tub" style="background:linear-gradient(#4a4a4a,#101010)"></div></div><div class="meta"><span>Items product title</span><span class="stars">★★★<span class="off">★★</span></span></div><span class="price">$50.00</span></div>
    <div class="card"><div class="thumb"><span class="badge new">NEW</span><div class="img" role="img" aria-label="Light wash jeans" style="background:linear-gradient(#bccbe0,#6b86ad)"></div></div><div class="meta"><span>Items product title</span><span class="stars">★★★<span class="off">★★</span></span></div><span class="price">$50.00</span></div>
    <div class="card"><div class="thumb"><div class="img" role="img" aria-label="Protein powder tub" style="background:linear-gradient(#444,#0e0e0e)"></div></div><div class="meta"><span>Items product title</span><span class="stars">★★★<span class="off">★★</span></span></div><span class="price">$50.00</span></div>
    <div class="card"><div class="thumb"><div class="img" role="img" aria-label="Red evening gown" style="background:linear-gradient(#e25a60,#a5202a)"></div></div><div class="meta"><span>Items product title</span><span class="stars">★★★<span class="off">★★</span></span></div><span class="price">$50.00</span></div>
    <div class="card"><div class="thumb"><span class="badge sale">SOLD OUT</span><div class="img" role="img" aria-label="Slim dark jeans" style="background:linear-gradient(#7d93b5,#34496d)"></div></div><div class="meta"><span>Items product title</span><span class="stars">★★★<span class="off">★★</span></span></div><span class="price">$50.00</span></div>
    <div class="card"><div class="thumb"><span class="badge new">NEW</span><div class="img" role="img" aria-label="White dress shirt" style="background:linear-gradient(#fafafa,#d4d8de)"></div></div><div class="meta"><span>Items product title</span><span class="stars">★★★<span class="off">★★</span></span></div><span class="price">$50.00</span></div>
  </div>

  <div class="pager"><span>Prev</span><span class="on">1</span><span>2</span><span>3</span><span>Next</span></div>
</div>

<section class="summer">
  <div class="clothes" role="img" aria-label="Denim shirt and jeans laid out" style="background:linear-gradient(120deg,#6e8fbf,#2e4a78)"></div>
  <div class="copy"><small>SPECIAL OFFER</small><h3>SUMMER SALE<br>GET IT NOW!</h3><p>DISCOUNT UP TO <b>50%</b></p></div>
  <div class="tub" role="img" aria-label="Large protein supplement tub" style="background:linear-gradient(#3d3d3d,#0c0c0c)"></div>
</section>

<div class="wrap">
  <div class="blog">
    <div class="blog-intro"><h2>Latest Blog</h2><p>Training tips, style notes and store news</p><a class="btn">VIEW ALL</a></div>
    <div class="post">
      <div class="img" role="img" aria-label="Shoppers carrying bags" style="background:linear-gradient(135deg,#d9c9c4,#5a3c3c)"></div>
      <div class="date">October 22, 2019</div>
      <h4>Lorem ipsum dolor sit amet</h4>
      <p>Simple ways to refresh your wardrobe this season without spending a fortune on new pieces.</p>
      <a class="more">READ MORE</a>
    </div>
    <div class="post">
      <div class="img" role="img" aria-label="Runner tying shoes on pavement" style="background:linear-gradient(135deg,#c9d1db,#4b4f57)"></div>
      <div class="date">October 22, 2019</div>
      <h4>Lorem ipsum dolor sit amet</h4>
      <p>How to build a steady training routine and pick the right protein to support recovery.</p>
      <a class="more">READ MORE</a>
    </div>
  </div>
</div>

<footer class="footer">
  <div class="wrap">
    <div class="top">
      <div class="brand"><span class="dot"></span>Bramblecrest</div>
      <div class="newsletter"><h5>NEWSLETTER</h5><p>Get offers and new arrivals straight to your inbox every week.</p></div>
      <div class="subscribe"><span class="field">Your email address</span><span class="go">SUBSCRIBE</span></div>
    </div>
    <div class="cols">
      <div class="col touch"><h6>GET IN TOUCH</h6><ul>
        <li><svg viewBox="0 0 14 14"><path d="M7 13s-4-4-4-7a4 4 0 0 1 8 0c0 3-4 7-4 7z"/><circle cx="7" cy="6" r="1.5"/></svg><span><b>ADDRESS</b>12 Harbor Lane, Fairview</span></li>
        <li><svg viewBox="0 0 14 14"><rect x="1" y="3" width="12" height="8"/><path d="M1 3l6 5 6-5"/></svg><span><b>MAIL US</b>hello@bramblecrest.example</span></li>
        <li><svg viewBox="0 0 14 14"><path d="M3 1h3l1 3-2 1a7 7 0 0 0 4 4l1-2 3 1v3c-6 1-11-4-10-10z"/></svg><span><b>PHONE</b>+1 800 555 0142</span></li>
      </ul></div>
      <div class="col std"><h6>PRODUCTS</h6><ul><li>Prices drop</li><li>New products</li><li>Best sales</li><li>Stores</li><li>Supplements</li><li>Blog</li></ul></div>
      <div class="col std"><h6>INFORMATION</h6><ul><li>Delivery</li><li>Legal notice</li><li>Terms of use</li><li>About us</li><li>Secure payment</li><li>Contact us</li></ul></div>
      <div class="col last"><h6>MY ACCOUNT</h6><ul><li>Sign in</li><li>My orders</li><li>Addresses</li><li>Wishlist</li></ul></div>
    </div>
  </div>
  <div class="bottom"><span>© Bramblecrest 2019. All rights reserved</span><div class="cards"><span></span><span></span><span></span><span></span></div><span>Privacy policy · Terms</span></div>
  <div class="totop"><svg viewBox="0 0 12 12"><path d="M2 8l4-4 4 4"/></svg></div>
</footer>

</body>
</html>
```